Business Card Design

We sell fish products to corporate food companies who then turn these products into final food products for consumers

Industry/Entity Type

Business

Contact Information for Business Card

I need a corporate business card template for a fish products business. We would like it be professional for use in dealing with multi national companies. This company business card template will be used by multiple employees so the following fields must be open to edit (Name, Phone Number and Email address)

```html
<!DOCTYPE html>
<html lang="en">
<head>
<meta charset="utf-8">
<title>Tidewater Catch – Business Card</title>
<link href="https://fonts.googleapis.com/css2?family=Lato:wght@300;400;700&display=swap" rel="stylesheet">
<style>
  :root {
    --backdrop: #e9e4dc;
    --card-black: #0a0b0d;
    --card-black-sheen: #2a2d33;
    --ocean-deep: #0d4f9e;
    --ocean-mid: #1a72c9;
    --ocean-light: #2aa9e0;
    --ocean-glow: #4fc6ee;
    --name-green: #a6dc7a;
    --text-white: #f2f7fb;
    --mark-blue: #3f9fe0;
  }
  * { margin: 0; padding: 0; box-sizing: border-box; }
  html, body { width: 1200px; height: 1022px; overflow: hidden; }
  body {
    background: var(--backdrop);
    font-family: "Lato", sans-serif;
    position: relative;
  }
  .card {
    position: absolute;
    width: 760px;
    height: 434px;
    border-radius: 26px;
    overflow: hidden;
    box-shadow: 0 14px 34px rgba(0,0,0,.22);
  }
  .card-front {
    left: 220px; top: 50px;
    background: linear-gradient(160deg, var(--card-black-sheen) 0%, var(--card-black) 45%, var(--card-black) 100%);
  }
  .card-back {
    left: 220px; top: 538px;
    background: linear-gradient(150deg, var(--ocean-mid) 0%, var(--ocean-deep) 100%);
  }
  .front-wave { position: absolute; inset: 0; }
  .front-brand {
    position: absolute;
    left: 36px; top: 204px;
    display: flex; align-items: center; gap: 10px;
    white-space: nowrap;
  }
  .brand-dot {
    width: 16px; height: 16px; border-radius: 50%;
    background: var(--mark-blue);
    flex: none;
  }
  .brand-name {
    font-weight: 400;
    font-size: 22px;
    letter-spacing: 1px;
    color: var(--mark-blue);
    text-transform: uppercase;
  }
  .contact {
    position: absolute;
    left: 452px; top: 120px;
    color: var(--text-white);
  }
  .contact-name {
    font-weight: 700;
    font-size: 24px;
    color: var(--name-green);
  }
  .contact-role {
    font-size: 19px;
    margin: 6px 0 0 92px;
  }
  .contact-line {
    display: flex; align-items: center; gap: 10px;
    font-size: 19px;
    margin-top: 40px;
  }
  .contact-line + .contact-line { margin-top: 16px; }
  .contact-line svg { width: 18px; height: 18px; fill: var(--text-white); flex: none; }
  .back-brand {
    position: absolute;
    inset: 0;
    display: flex; align-items: center; justify-content: center; gap: 22px;
  }
  .back-brand .brand-dot { width: 34px; height: 34px; background: var(--ocean-glow); }
  .back-brand .brand-name { font-size: 50px; letter-spacing: 5px; color: var(--ocean-glow); font-weight: 300; }
</style>
</head>
<body>
  <section class="card card-front" aria-label="Card front">
    <svg class="front-wave" viewBox="0 0 760 434" aria-hidden="true">
      <defs>
        <linearGradient id="waveFill" x1="0" y1="0" x2="1" y2="1">
          <stop offset="0" stop-color="#2ab6e6"/>
          <stop offset="1" stop-color="#1262b8"/>
        </linearGradient>
      </defs>
      <ellipse cx="770" cy="217" rx="455" ry="330" fill="#3cc3ee"/>
      <ellipse cx="775" cy="225" rx="428" ry="318" fill="url(#waveFill)"/>
    </svg>
    <div class="front-brand">
      <span class="brand-dot"></span>
      <span class="brand-name">Tidewater Catch</span>
    </div>
    <div class="contact">
      <p class="contact-name">Marcus Lee Harlan</p>
      <p class="contact-role">Director</p>
      <p class="contact-line">
        <svg viewBox="0 0 24 24" aria-hidden="true"><path d="M6.6 10.8a15.1 15.1 0 0 0 6.6 6.6l2.2-2.2a1 1 0 0 1 1-.25 11.4 11.4 0 0 0 3.6.57 1 1 0 0 1 1 1V20a1 1 0 0 1-1 1A17 17 0 0 1 3 4a1 1 0 0 1 1-1h3.5a1 1 0 0 1 1 1c0 1.25.2 2.45.57 3.570a1 1 0 0 1-.25 1z"/></svg>
        (555) 014 2290
      </p>
      <p class="contact-line">
        <svg viewBox="0 0 24 24" aria-hidden="true"><path d="M3 5h18v14H3zm2 2v.5l7 4.5 7-4.5V7zm0 2.9V17h14V9.9l-7 4.5z"/></svg>
        hello@tidewatercatch.com
      </p>
    </div>
  </section>

  <section class="card card-back" aria-label="Card back">
    <div class="back-brand">
      <span class="brand-dot"></span>
      <span class="brand-name">Tidewater Catch</span>
    </div>
  </section>
</body>
</html>
```